Redesign website for Sunny Casas

Sunny Casas Algarve (www.sunnycasasalgarve-example.com) is a vacation rental company based in Algarve, Portugal.
We want to redesign our website for a more modern and responsive version.

We do like something like this: https://www.plushhideaways-example.com, https://www.tidalkeyhomes-example.com, http://www.moraspropertyqx-example.com, and https://www.kelvatrum-example.com

We would prefer the use of a Wordpress theme specific for vacation rentals, that already has the tools that we need: reservations, availability sync via Ical, and payments.

Target Market(s)

The website must be appealing to guests who book directly, and to property owners, who deliver their villas to our portfolio.

Industry/Entity Type

Accommodation

Coding

Coded - Design and coding required

Font styles to use
Sans Serif

Colors
33a6d7
85cae6
cee9f5
cfeae6
86cfc6

Requirements
Must have
• A summery and holiday look

```html
<!DOCTYPE html>
<html lang="en">
<head>
<meta charset="utf-8">
<title>Sunny Casas – the Algarve holiday collection</title>
<link rel="stylesheet" href="https://fonts.googleapis.com/css2?family=Montserrat:wght@400;500;600;700&display=swap">
<style>
:root{
  --blue:#33a6d7;
  --blue-light:#85cae6;
  --blue-pale:#cee9f5;
  --teal:#86cfc6;
  --teal-pale:#cfeae6;
  --ink:#222;
  --ink-soft:#555;
  --muted:#8a8f94;
  --dark:#1c1c1c;
  --white:#fff;
  --line:#e3e6e8;
}
*{box-sizing:border-box;margin:0;padding:0}
html,body{width:1200px;height:3442px;overflow:hidden}
body{font-family:"Montserrat",sans-serif;color:var(--ink);background:var(--white);position:relative}
a{color:inherit;text-decoration:none}

/* Hero */
.hero{position:absolute;left:0;top:0;width:1200px;height:608px;
  background:linear-gradient(180deg,#1b2a4a 0%,#3b4a5e 30%,#8a6a3e 55%,#2a3550 80%,#16213a 100%)}
.hero .photo{position:absolute;inset:0}
.nav{position:absolute;top:0;left:0;width:1200px;height:100px;display:flex;align-items:center;padding:0 87px;
  background:linear-gradient(180deg,rgba(10,18,40,.6),rgba(10,18,40,0))}
.brand{font-size:33px;font-weight:500;letter-spacing:3px;color:var(--white);text-transform:uppercase;white-space:nowrap}
.menu{margin-left:auto;display:flex;gap:38px;font-size:14px;font-weight:500;color:var(--white)}
.menu .lang::after{content:"";display:inline-block;margin-left:8px;border:5px solid transparent;border-top-color:var(--white);vertical-align:-2px}
.hero-title{position:absolute;top:268px;width:100%;text-align:center;color:var(--white);font-size:38px;font-weight:700}
.hero-sub{position:absolute;top:318px;width:100%;text-align:center;color:var(--white);font-size:18px;font-weight:500}
.search{position:absolute;top:363px;left:103px;display:flex;height:55px}
.search .field{background:var(--white);height:55px;display:flex;align-items:center;gap:12px;padding:0 22px;font-size:15px;color:var(--muted);font-style:italic;border-right:1px solid var(--line);white-space:nowrap}
.search .where{width:318px}
.search .date{width:158px;justify-content:center}
.search .guests{width:181px;justify-content:space-between}
.search .btn{margin-left:21px;width:158px;height:55px;background:var(--blue);color:var(--white);font-size:17px;font-weight:600;display:flex;align-items:center;justify-content:center;letter-spacing:1px}

/* Amenities */
.amenities{position:absolute;top:608px;left:0;width:1200px;height:191px;background:var(--blue)}
.amenity{position:absolute;top:42px;height:107px;border:2px solid var(--white);color:var(--white);display:flex;flex-direction:column;align-items:center;justify-content:flex-end;padding-bottom:10px;gap:12px;font-size:16px;font-weight:600}
.amenity svg{width:70px;height:56px}

/* Featured */
.section-title{position:absolute;width:100%;text-align:center;font-size:32px;font-weight:500;color:#333}
.rule{position:absolute;left:564px;width:72px;height:3px;background:var(--blue)}
.card{position:absolute;width:331px}
.card h3{font-size:22px;font-weight:600;color:#222;padding-left:20px;height:28px;white-space:nowrap}
.card .addr{font-size:12px;color:var(--muted);padding-left:22px;height:25px}
.card .image{position:relative;width:331px;height:214px}
.badge{position:absolute;top:0;right:10px;width:92px;height:34px;background:var(--dark);color:var(--white);font-size:13px;font-weight:600;display:flex;align-items:center;justify-content:center}
.badge.blue{background:var(--blue)}
.specs{display:grid;grid-template-columns:1fr 1fr;row-gap:10px;padding:18px 22px 14px;font-size:12px;color:var(--muted);border-bottom:1px solid var(--line)}
.specs span{display:flex;align-items:center;gap:14px}
.specs svg{width:16px;height:14px;fill:#9aa0a5}
.price-row{display:flex;justify-content:space-between;align-items:center;padding:14px 30px 0 30px}
.price{font-size:19px;font-weight:600;color:var(--blue)}
.more{width:125px;height:32px;background:var(--dark);color:var(--white);font-size:12px;font-weight:700;display:flex;align-items:center;justify-content:center}
.more.blue{background:var(--blue)}

/* Events & Attractions */
.promo{position:absolute;top:1960px;height:470px;width:600px;color:var(--white);padding:50px 0 0 84px}
.promo.events{left:0;background:linear-gradient(180deg,#1f2a34 0%,#3a4650 45%,#c9c9cc 75%,#6b6e74 100%)}
.promo.attractions{left:600px;padding-left:45px;background:linear-gradient(180deg,#0f1e3a 0%,#1c3a5c 50%,#2c5a7a 75%,#0d1a30 100%)}
.promo h2{font-size:70px;font-weight:600;line-height:1}
.promo p{margin-top:22px;width:500px;font-size:15px;font-weight:600;line-height:1.7}
.promo .btn{display:flex;align-items:center;justify-content:center;margin-top:26px;width:206px;height:48px;background:var(--blue);font-size:16px;font-weight:500;margin-left:8px}
.promo.attractions .btn{background:var(--teal);margin-left:0}

/* Testimonials */
.quote{position:absolute;top:2622px;width:460px;text-align:center;font-size:13px;line-height:1.95;color:#666}
.avatar{position:absolute;top:2724px;width:64px;height:64px;border-radius:50%;background:radial-gradient(circle at 50% 40%,#e8d1bf,#b58a6a)}
.person{position:absolute;top:2808px;width:300px;text-align:center;font-size:16px;color:var(--blue);font-weight:500}
.get-started{position:absolute;top:2912px;left:445px;width:299px;height:58px;background:var(--blue);color:var(--white);display:flex;align-items:center;justify-content:center;font-size:17px;font-weight:500}

/* Newsletter */
.newsletter{position:absolute;top:3059px;left:0;width:1200px;height:115px;background:var(--blue-light);color:var(--white)}
.newsletter h2{position:absolute;left:87px;top:24px;font-size:30px;font-weight:600}
.newsletter p{position:absolute;left:87px;top:66px;font-size:12px;font-weight:500}
.newsletter .email{position:absolute;left:567px;top:36px;width:364px;height:44px;background:var(--white);color:#333;font-size:13px;font-weight:500;display:flex;align-items:center;padding-left:22px}
.newsletter .submit{position:absolute;left:944px;top:36px;width:127px;height:44px;background:var(--blue);font-size:16px;font-weight:600;display:flex;align-items:center;justify-content:center}

/* Footer */
.footer{position:absolute;top:3174px;left:0;width:1200px;height:268px;background:var(--blue);color:var(--white)}
.footer .brand{position:absolute;left:87px;top:70px;font-size:44px}
.footer h4{position:absolute;left:464px;top:34px;font-size:24px;font-weight:600}
.contact{position:absolute;top:102px;left:464px;display:flex;gap:30px;font-size:12px;white-space:nowrap}
.contact span{display:flex;align-items:center;gap:9px}
.contact svg{width:14px;height:16px;fill:var(--white);flex:none}
.social{position:absolute;left:464px;top:148px;display:flex;gap:16px}
.social i{display:block;width:14px;height:14px;border-radius:50%;background:var(--white)}
.legal{position:absolute;left:87px;top:230px;display:flex;font-size:11px;font-weight:500;white-space:nowrap}
.legal a+a::before{content:"|";margin:0 16px}
.copyright{position:absolute;right:100px;top:230px;font-size:11px}
</style>
</head>
<body>

<header class="hero">
  <div class="photo" role="img" aria-label="Evening view of a lit Algarve villa with pool and terraces"></div>
  <nav class="nav">
    <a class="brand" href="#">Sunny Casas</a>
    <div class="menu">
      <a href="#">Home</a><a href="#">Holiday Rentals</a><a href="#">What to Do</a><a href="#">Guest Services</a><a href="#">Reviews</a><a class="lang" href="#">English</a>
    </div>
  </nav>
  <h1 class="hero-title">SUNNY CASAS - the Algarve holiday collection</h1>
  <p class="hero-sub">Holiday villas &amp; Apartments in Algarve</p>
  <form class="search">
    <div class="field where"><svg width="12" height="16" viewBox="0 0 12 16"><path d="M6 0a6 6 0 0 0-6 6c0 4.5 6 10 6 10s6-5.5 6-10a6 6 0 0 0-6-6zm0 8.5A2.5 2.5 0 1 1 6 3.5a2.5 2.5 0 0 1 0 5z" fill="#555"/></svg>Where do you want to go?</div>
    <div class="field date">Check In <svg width="14" height="14" viewBox="0 0 14 14"><rect x="1" y="2" width="12" height="11" fill="none" stroke="#666" stroke-width="1.5"/><path d="M1 5h12" stroke="#666" stroke-width="1.5"/></svg></div>
    <div class="field date">Check Out <svg width="14" height="14" viewBox="0 0 14 14"><rect x="1" y="2" width="12" height="11" fill="none" stroke="#666" stroke-width="1.5"/><path d="M1 5h12" stroke="#666" stroke-width="1.5"/></svg></div>
    <div class="field guests">1 Guest <svg width="16" height="16" viewBox="0 0 16 16"><circle cx="8" cy="8" r="7" fill="#444"/><path d="M8 4v8M4 8h8" stroke="#fff" stroke-width="2"/></svg></div>
    <div class="btn">SEARCH</div>
  </form>
</header>

<section class="amenities">
  <div class="amenity" style="left:119px;width:124px">
    <svg viewBox="0 0 70 56" fill="none" stroke="#fff" stroke-width="6" stroke-linecap="round"><path d="M8 20a38 38 0 0 1 54 0"/><path d="M18 31a24 24 0 0 1 34 0"/><path d="M27 41a11 11 0 0 1 16 0"/><circle cx="35" cy="49" r="3" fill="#fff"/></svg>WiFi</div>
  <div class="amenity" style="left:250px;width:204px">
    <svg viewBox="0 0 70 56" fill="none" stroke="#fff" stroke-width="3.5"><rect x="10" y="10" width="50" height="20" rx="4"/><rect x="15" y="16" width="17" height="10" rx="3"/><rect x="38" y="16" width="17" height="10" rx="3"/><rect x="5" y="30" width="60" height="14" rx="2"/><path d="M9 44v8M61 44v8"/></svg>Fully Furnished</div>
  <div class="amenity" style="left:459px;width:204px">
    <svg viewBox="0 0 70 56"><rect x="14" y="2" width="42" height="52" rx="7" fill="#fff"/><path d="M28 44V14h9a8 8 0 0 1 0 16h-9" fill="none" stroke="#33a6d7" stroke-width="6"/></svg>Free Parking</div>
  <div class="amenity" style="left:668px;width:205px">
    <svg viewBox="0 0 70 56" fill="#fff"><path d="M4 30l8-2 6 6 14-4-10-20 6-2 18 18 14-4c4-1 6 3 2 5L16 40 4 30z"/><rect x="6" y="48" width="58" height="3"/></svg>Airport Transfers</div>
  <div class="amenity" style="left:879px;width:205px">
    <svg viewBox="0 0 70 56" fill="#fff"><path d="M14 22h34l-4 32H18z"/><rect x="44" y="2" width="4" height="26" transform="rotate(20 46 15)"/><path d="M52 26l8 10-10 4z"/><circle cx="20" cy="14" r="4"/><circle cx="28" cy="10" r="3"/></svg>Cleaning Services</div>
</section>

<h2 class="section-title" style="top:864px">Featured Properties</h2>
<div class="rule" style="top:921px"></div>

<svg width="0" height="0" style="position:absolute">
  <defs>
    <symbol id="i-area" viewBox="0 0 16 14"><path d="M2 12L14 2M2 12h5M2 12V7M14 2H9M14 2v5" stroke="#9aa0a5" stroke-width="1.6" fill="none"/></symbol>
    <symbol id="i-bed" viewBox="0 0 16 14"><rect x="1" y="3" width="3" height="9"/><rect x="4" y="7" width="11" height="3"/><rect x="13" y="7" width="2" height="5"/></symbol>
    <symbol id="i-car" viewBox="0 0 16 14"><path d="M3 5l2-4h6l2 4h2v6h-2v2h-2v-2H5v2H3v-2H1V5z"/></symbol>
    <symbol id="i-bath" viewBox="0 0 16 14"><rect x="1" y="6" width="14" height="3"/><path d="M2 9h12l-2 4H4z"/><rect x="3" y="1" width="2" height="5"/></symbol>
  </defs>
</svg>

<article class="card" style="left:87px;top:980px">
  <h3>Lagos Sunbird</h3><p class="addr">&#9679; 1420 Marlow Lane, Faro</p>
  <div class="image" role="img" aria-label="Bright living room with sofa, armchair and terrace doors" style="background:linear-gradient(160deg,#e9e3d6,#c9b79a 45%,#6b4a32)"><span class="badge">NEW</span></div>
  <div class="specs"><span><svg><use href="#i-area"/></svg>1568 Sq</span><span><svg><use href="#i-bed"/></svg>2 Bedrooms</span><span><svg><use href="#i-car"/></svg>1 Garages</span><span><svg><use href="#i-bath"/></svg>5 Bathrooms</span></div>
  <div class="price-row"><span class="price">€50</span><a class="more" href="#">MORE DETAILS</a></div>
</article>

<article class="card" style="left:436px;top:980px">
  <h3>Apartment Bay View</h3><p class="addr">&#9679; 1420 Marlow Lane, Faro</p>
  <div class="image" role="img" aria-label="Balcony dining table with sea view" style="background:linear-gradient(160deg,#bfd8ea,#d3a67a 45%,#5a3a26)"><span class="badge blue">NEW</span></div>
  <div class="specs"><span><svg><use href="#i-area"/></svg>2000 Sq</span><span><svg><use href="#i-bed"/></svg>3 Bedrooms</span><span><svg><use href="#i-car"/></svg>2 Garages</span><span><svg><use href="#i-bath"/></svg>5 Bathrooms</span></div>
  <div class="price-row"><span class="price">€50</span><a class="more blue" href="#">MORE DETAILS</a></div>
</article>

<article class="card" style="left:783px;top:980px">
  <h3>Albufeira Sunset</h3><p class="addr">&#9679; 1420 Marlow Lane, Faro</p>
  <div class="image" role="img" aria-label="Pool terrace with yellow umbrellas and loungers" style="background:linear-gradient(170deg,#6aa84f,#e0c13a 40%,#3d9bd0 70%,#2a6e9e)"><span class="badge">NEW</span></div>
  <div class="specs"><span><svg><use href="#i-area"/></svg>2500 Sq</span><span><svg><use href="#i-bed"/></svg>4 Bedrooms</span><span><svg><use href="#i-car"/></svg>3 Garages</span><span><svg><use href="#i-bath"/></svg>8 Bathrooms</span></div>
  <div class="price-row"><span class="price">€79</span><a class="more" href="#">MORE DETAILS</a></div>
</article>

<article class="card" style="left:87px;top:1432px">
  <h3>Villa Marco</h3><p class="addr">&#9679; 1420 Marlow Lane, Faro</p>
  <div class="image" role="img" aria-label="Shaded garden patio with seating under trees" style="background:linear-gradient(170deg,#a7c07a,#5e7a3a 45%,#8a6a4a)"><span class="badge">NEW</span></div>
  <div class="specs"><span><svg><use href="#i-area"/></svg>2568 Sq</span><span><svg><use href="#i-bed"/></svg>3 Bedrooms</span><span><svg><use href="#i-car"/></svg>2 Garages</span><span><svg><use href="#i-bath"/></svg>5 Bathrooms</span></div>
  <div class="price-row"><span class="price">€79</span><a class="more" href="#">MORE DETAILS</a></div>
</article>

<article class="card" style="left:436px;top:1432px">
  <h3>Vilamoura Terrace</h3><p class="addr">&#9679; 1420 Marlow Lane, Faro</p>
  <div class="image" role="img" aria-label="Modern white apartment block with pool and palm trees" style="background:linear-gradient(180deg,#2f7fd6,#8fc3ea 40%,#e8eef2 55%,#2aa0d8 70%,#5aa83a)"><span class="badge">NEW</span></div>
  <div class="specs"><span><svg><use href="#i-area"/></svg>2568 Sq</span><span><svg><use href="#i-bed"/></svg>3 Bedrooms</span><span><svg><use href="#i-car"/></svg>3 Garages</span><span><svg><use href="#i-bath"/></svg>5 Bathrooms</span></div>
  <div class="price-row"><span class="price">€82</span><a class="more" href="#">MORE DETAILS</a></div>
</article>

<article class="card" style="left:783px;top:1432px">
  <h3>Bright family apartment</h3><p class="addr">&#9679; 1420 Marlow Lane, Faro</p>
  <div class="image" role="img" aria-label="Apartment building beside a large blue pool" style="background:linear-gradient(180deg,#4a9be0,#b9d9f0 35%,#efe9df 50%,#1f78c8 75%,#1a5fa8)"><span class="badge">NEW</span></div>
  <div class="specs"><span><svg><use href="#i-area"/></svg>2568 Sq</span><span><svg><use href="#i-bed"/></svg>3 Bedrooms</span><span><svg><use href="#i-car"/></svg>2 Garages</span><span><svg><use href="#i-bath"/></svg>5 Bathrooms</span></div>
  <div class="price-row"><span class="price">$86892.00</span><a class="more" href="#">MORE DETAILS</a></div>
</article>

<section class="promo events" role="img" aria-label="Elegant table setting for a wedding dinner">
  <h2>Events</h2>
  <p>Our unique selection of sunny Algarve holiday villas have that little something to exceptional private wedding venues.</p>
  <a class="btn" href="#">View Collection</a>
</section>
<section class="promo attractions" role="img" aria-label="Dolphins swimming in deep blue water">
  <h2>Attractions</h2>
  <p>The excellent weather that is felt throughout the year and the beautiful beaches make the Algarve a beloved destina-</p>
  <a class="btn" href="#">View Collection</a>
</section>

<h2 class="section-title" style="top:2502px">Our Thousands of Happy Customers</h2>
<div class="rule" style="top:2563px"></div>

<p class="quote" style="left:110px">“Lorem Ipsum is simply dummy text of the printing and typesetting industry. Lorem Ipsum has been the industry's standard dummy text ever since the 1500s, and scrambled it to make a type specimen book. It has survived not only five centuries.”</p>
<div class="avatar" style="left:304px" role="img" aria-label="Guest portrait"></div>
<p class="person" style="left:186px">Marta C Reyes</p>

<p class="quote" style="left:635px">“Lorem Ipsum is simply dummy text of the printing and typesetting industry. Lorem Ipsum has been the industry's standard dummy text ever since the 1500s, and scrambled it to make a type specimen book. It has survived not only five centuries.”</p>
<div class="avatar" style="left:833px" role="img" aria-label="Guest portrait"></div>
<p class="person" style="left:715px">Marta C Reyes</p>

<a class="get-started" href="#">GET STARTED</a>

<section class="newsletter">
  <h2>Join Our Newsletter</h2>
  <p>Sign up to receive timely, useful information in your inbox.</p>
  <div class="email">EMAIL</div>
  <div class="submit">SUBMIT</div>
</section>

<footer class="footer">
  <div class="brand">Sunny Casas</div>
  <h4>To Reach Us:</h4>
  <div class="contact">
    <span><svg viewBox="0 0 12 16"><path d="M6 0a6 6 0 0 0-6 6c0 4.5 6 10 6 10s6-5.5 6-10a6 6 0 0 0-6-6zm0 8.5A2.5 2.5 0 1 1 6 3.5a2.5 2.5 0 0 1 0 5z"/></svg>Rua do Sol, Lote 12B, Albufeira</span>
    <span><svg viewBox="0 0 16 16"><path d="M3 1l3 0 1.5 4-2 1.5a9 9 0 0 0 4 4L11 8.5l4 1.5v3a2 2 0 0 1-2 2A13 13 0 0 1 1 3a2 2 0 0 1 2-2z"/></svg>+351 900 000 147</span>
    <span><svg viewBox="0 0 16 12"><path d="M0 0h16v12H0z" fill="#fff"/><path d="M0 0l8 7 8-7" stroke="#33a6d7" stroke-width="1.5" fill="none"/></svg>info@sunnycasasalgarve-example.com</span>
  </div>
  <div class="social"><i></i><i></i><i></i><i></i><i></i></div>
  <nav class="legal"><a href="#">About Us</a><a href="#">Terms &amp; Conditions</a><a href="#">List your Property</a><a href="#">Buy a Rental Property</a><a href="#">Rent a Car</a><a href="#">Contact Us</a></nav>
  <p class="copyright">Copyright © 2018. Sunny Casas.</p>
</footer>

</body>
</html>
```